Brovanta Energy Ratings Whole Home Energy Rating Flyer

Please create a flyer 8.5" x 11" that is 2-sided that goes hand and hand with my tri-fold flyer. The flyer will target prospective homeowners and real estate agents to purchase a whole home energy rating. I have attached further details.

Target Market(s)

Homeowners looking to remodel their homes, save on energy bills, purchase or sell a home.

Font styles to use
Serif
Sans Serif

Colors
3176b5
ffffff

Requirements
Must have
• Must be able to sell a whole home energy rating on its own!
Nice to have
• I would like to mimic the colors and background of my tri-fold flyer.
Should not have
• Should not be boring!

```html
<!DOCTYPE html>
<html lang="en">
<head>
<meta charset="utf-8">
<title>Brovanta Energy Ratings – Whole Home Energy Rating Flyer</title>
<link href="https://fonts.googleapis.com/css2?family=Lato:wght@400;700;900&display=swap" rel="stylesheet">
<style>
:root{
  --brand:#3176b5;
  --brand-deep:#1f5fa8;
  --brand-light:#8fb4dc;
  --navy:#17305a;
  --ink:#222831;
  --white:#ffffff;
  --stage:#3b3b3b;
  --sky-top:#c4dcf1;
  --sky-bottom:#5d98d0;
}
*{box-sizing:border-box;margin:0;padding:0}
html,body{width:834px;height:1200px;overflow:hidden}
body{background:var(--stage);font-family:'Lato',Arial,sans-serif;color:var(--ink);position:relative}
.page{position:absolute;left:193px;width:448px;height:580px;background:var(--white);overflow:hidden;box-shadow:0 4px 14px rgba(0,0,0,.45)}
.page--front{top:14px}
.page--back{top:606px}
.abs{position:absolute}

/* front */
.photo{left:0;top:0;width:448px;height:250px;background:linear-gradient(160deg,var(--sky-top) 0%,#8fb9e2 45%,var(--sky-bottom) 100%);clip-path:polygon(0 0,100% 0,100% 66%,0 94%)}
.logo-card{left:22px;top:0;width:182px;height:100px;background:var(--white);box-shadow:2px 3px 8px rgba(0,0,0,.25);display:flex;flex-direction:column;justify-content:center;padding-left:26px}
.logo-name{display:flex;align-items:center;gap:6px;font-weight:900;font-size:20px;letter-spacing:.5px;color:var(--navy);line-height:1}
.logo-name i{width:10px;height:10px;background:var(--brand);display:block}
.logo-sub{font-size:6.5px;font-weight:700;letter-spacing:1px;color:var(--brand);margin-left:16px;margin-top:3px}
.intro{left:20px;top:266px;width:412px;font-size:8px;line-height:1.3;color:var(--brand-deep);font-weight:700}
.section{left:14px;width:420px}
.section h3{font-size:7.6px;font-weight:700;color:var(--navy);display:flex;align-items:center;gap:6px;margin-bottom:4px;line-height:1.2}
.section h3::before{content:"";width:5px;height:5px;background:var(--brand-deep);display:block;flex:none}
.section p{font-size:5.5px;line-height:1.36;margin-left:9px;margin-bottom:5px;text-align:justify}
.contact{left:18px;top:508px;color:var(--white);font-size:7px;line-height:1.5}
.contact strong{font-size:7.8px;display:block;margin-bottom:2px}
.contact span{display:flex;align-items:center;gap:5px}
.contact svg{width:7px;height:7px;flex:none}
.follow{right:18px;top:526px;color:var(--white);text-align:right;font-size:7.5px;font-weight:700}
.social{display:flex;gap:6px;margin-top:6px}
.social b{width:14px;height:14px;border:1px solid var(--white);border-radius:50%;display:block}

/* back */
.illustration{left:296px;top:16px;width:136px;height:98px;border-radius:4px;background:linear-gradient(135deg,#e6e0d6 0%,#c9b79b 40%,#7fc34b 65%,#f0a020 85%,#d8352a 100%)}
.back-logo{left:54px;top:30px}
.back-logo .logo-name{color:var(--white);font-size:16px}
.back-logo .logo-name i{background:var(--white);width:9px;height:9px}
.back-logo .logo-sub{color:var(--white);font-size:5.5px;margin-left:15px}
.checklist{left:30px;top:172px;width:400px;display:grid;grid-template-columns:1.15fr 1.45fr 1fr;row-gap:5px;font-size:6.4px;list-style:none}
.checklist li{display:flex;align-items:center;gap:4px}
.checklist li::before{content:"\2713";color:var(--brand-deep);font-weight:900;font-size:7px}
.notes{left:20px;top:245px;width:412px;font-size:5.2px;line-height:1.35}
.notes p{margin-bottom:8px}
.reviews{left:0;top:370px;width:448px;height:138px;background:var(--brand-deep);color:var(--white);padding:6px 20px}
.reviews h4{text-align:center;font-size:7.3px;font-weight:700;margin-bottom:6px}
.quote{font-size:5.4px;line-height:1.35;position:relative;padding-top:9px;margin-bottom:6px;text-align:justify}
.quote::before{content:"\201C";position:absolute;left:0;top:-6px;font-size:18px;font-weight:900;line-height:1.2}
.quote cite{display:block;text-align:right;font-style:italic;padding-right:22px;margin-top:2px;position:relative}
.quote cite::after{content:"\201D";position:absolute;right:0;top:-2px;font-size:18px;font-weight:900;font-style:normal;line-height:1}
.target-line{left:20px;top:520px;font-size:5.6px}
.back-social{right:18px;top:514px;display:flex;gap:6px}
.back-social b{width:14px;height:14px;border:1px solid var(--ink);border-radius:50%;display:block}
.rule{left:14px;top:534px;width:420px;height:1px;background:#cfd7e2}
.footer-bar{left:0;top:542px;width:448px;height:38px;background:var(--brand-deep);color:var(--white);font-size:6px;display:flex;align-items:center;justify-content:space-around;padding:0 10px}
.footer-bar span{display:flex;align-items:center;gap:4px}
.footer-bar span+span{border-left:1px solid rgba(255,255,255,.6);padding-left:18px}
.footer-bar svg{width:7px;height:7px;flex:none}
</style>
</head>
<body>

<section class="page page--front">
  <div class="abs photo" role="img" aria-label="Photo of a worker in a hard hat installing solar panels on a roof"></div>
  <svg class="abs" style="left:0;top:0" width="448" height="580" viewBox="0 0 448 580" aria-hidden="true">
    <polygon points="0,226 448,152 448,160 0,234" fill="#8fb4dc"/>
    <polygon points="0,236 448,162 448,176 0,250" fill="#1f5fa8"/>
    <polygon points="0,488 448,462 448,466 0,492" fill="#8fb4dc"/>
    <polygon points="0,498 448,470 448,580 0,580" fill="#1f5fa8"/>
    <polygon points="200,580 448,520 448,580" fill="#111"/>
  </svg>
  <div class="abs logo-card">
    <div class="logo-name"><i></i>BROVANTA</div>
    <div class="logo-sub">ENERGY RATINGS</div>
  </div>
  <p class="abs intro">Would you like to lower your monthly energy bill, enjoy a safer, more comfortable and durable home, and increase your homes appraisal value and sales appeal? Then keep reading, because that is what a lost cost, home energy rating can do for you...</p>
  <div class="abs section" style="top:304px">
    <h3>What is a Whole Home Energy Rating?</h3>
    <p>A Whole Home Energy Rating is a comprehensive evaluation of the efficiency of the entire home. You will receive a written report that includes a numeric score or "rating" of the home, plus recommendations for improvements that will reduce energy bills and make the home more comfortable. Each rating will receive an official California Home Energy Rating Certificate and home energy rating report with the State Energy Board's (SEB) seal. The report will identify the most cost-effective and appropriate energy efficiency improvements needed to save you money and provide long lasting comfort.</p>
    <h3>Who needs a Whole Home Energy Rating?</h3>
    <p>- Everyone! Whether you are buying or selling, or plan on staying in your home for one year or the rest of your life, each whole home energy rating is geared toward helping you save money, and is custom tailored to fit your unique needs. The whole home energy rating can be designed to fit any lifestyle or energy improvement budget, with a focal point on cost effectiveness and common sense.</p>
    <p>- Buyers who choose to get a whole home energy rating can better decide which home will save them money through energy efficiency! They may also be entitled to federal tax credits, and borrow up to $40,000 for energy improvements through their mortgage.</p>
    <p>- Sellers who have a SEB certificate showing their homes energy efficiency ultimately make their homes more valuable and often sell their homes faster than those without documentation.</p>
    <p>- Before you remodel your home, make sure you have a HERS Rater conduct a Whole Home Energy Rating so you know exactly where to focus your money.</p>
  </div>
  <div class="abs contact">
    <strong>Contact Info</strong>
    <span><svg viewBox="0 0 10 10"><path d="M5 0a3.5 3.5 0 0 0-3.5 3.5C1.5 6 5 10 5 10s3.5-4 3.5-6.5A3.5 3.5 0 0 0 5 0z" fill="#fff"/></svg>Lindale, CA</span>
    <span><svg viewBox="0 0 10 10"><path d="M2 0l2 2.5-1 1.5a6 6 0 0 0 3 3l1.5-1L10 8l-1.5 2C4 10 0 6 0 1.5z" fill="#fff"/></svg>(555) 410-2287</span>
    <span><svg viewBox="0 0 10 10"><rect x=".5" y="2" width="9" height="6" fill="none" stroke="#fff"/><path d="M.5 2L5 5.5 9.5 2" fill="none" stroke="#fff"/></svg>info@BrovantaRatings.com</span>
    <span><svg viewBox="0 0 10 10"><circle cx="5" cy="5" r="4.5" fill="none" stroke="#fff"/><path d="M.5 5h9M5 .5v9" stroke="#fff"/></svg>www.BrovantaRatings.com</span>
  </div>
  <div class="abs follow">Follow Us<div class="social"><b></b><b></b><b></b><b></b></div></div>
</section>

<section class="page page--back">
  <svg class="abs" style="left:0;top:0" width="448" height="110" viewBox="0 0 448 110" aria-hidden="true">
    <polygon points="0,40 164,92 448,40 448,50 164,102 0,50" fill="#8fb4dc"/>
    <polygon points="0,0 448,0 448,40 164,92 0,40" fill="#1f5fa8"/>
    <polygon points="0,0 150,0 0,36" fill="#3176b5"/>
  </svg>
  <div class="abs back-logo">
    <div class="logo-name"><i></i>BROVANTA</div>
    <div class="logo-sub">ENERGY RATINGS</div>
  </div>
  <div class="abs illustration" role="img" aria-label="Illustration of a cutaway house with an energy efficiency rating scale"></div>
  <div class="abs section" style="top:110px">
    <h3>Who performs the rating?</h3>
    <p>A Home Energy Rating System (HERS) Rater, who is certified by the SEB will conduct the rating. Each California HERS Rater must follow standardized energy auditing procedures and use energy analysis software that meets SEB requirements.</p>
    <h3>The HERS Rater will inspect and assess all the major energy efficiency features of your home:</h3>
  </div>
  <ul class="abs checklist">
    <li>Air leaks</li><li>Water heating system</li><li>Major appliances</li>
    <li>Cooling system</li><li>Insulation (attic, walls, floor, roof)</li><li>Solar (if any)</li>
    <li>Heating system</li><li>Windows</li><li>Other energy uses</li>
    <li>Cooling/heating duct system</li><li>Lighting</li><li>Prior energy bills</li>
  </ul>
  <div class="abs notes">
    <p>- Every report is custom tailored to each unique home.</p>
    <p>- Brovanta Energy Ratings includes a free duct leakage test and free building envelope leakage test with each home energy audit.</p>
    <p>- Heating and cooling ducts in an average California home leak almost 30 percent. That is why when heating or cooling equipment is replaced, testing the system's ducts for leaks is now required by building officials in many parts of the state.</p>
    <p>- You wouldn't buy a new car without knowing the "miles per gallon", so why buy a home without knowing the "home energy rating?"</p>
    <p>- After your mortgage payment, your energy bill is often the second largest monthly home ownership expense.</p>
    <p>- Combine an Energy Efficient Mortgage (EEM) with other programs and you may be able to borrow up to $40,000 or more for efficiency improvements. Ask a knowledgeable lender if an EEM is right for you.</p>
  </div>
  <div class="abs reviews">
    <h4>Customer Reviews:</h4>
    <div class="quote">I had the pleasure of hiring Brovanta to perform a home energy audit on my home and I was truly amazed by the level of professionalism and the great service I received from Dan Norell. The audit report he provided me was very complete and informative. It allowed me to make informed financial decision regarding repairs to my home. After providing me the report he call me to explain everything in it and suggested various item to make my home more energy efficient. Mr. Norell is a wealth of knowledge and I will highly recommend it to any homeowner.<cite>- Marco P.</cite></div>
    <div class="quote">While having my air conditioning replaced, my ac contractor called this company to do the duct test. Mr. Norell arrived right on time, and explained the process thoroughly. He was clean and efficient while working throughout the house. He put my mind at ease during the process. I would definitely recommend this company.<cite>- Helen R.</cite></div>
  </div>
  <p class="abs target-line">Search "whole home energy ratings California" for details on what I am targeting.</p>
  <div class="abs back-social"><b></b><b></b><b></b><b></b></div>
  <div class="abs rule"></div>
  <div class="abs footer-bar">
    <span><svg viewBox="0 0 10 10"><path d="M5 0a3.5 3.5 0 0 0-3.5 3.5C1.5 6 5 10 5 10s3.5-4 3.5-6.5A3.5 3.5 0 0 0 5 0z" fill="#fff"/></svg>Lindale, CA</span>
    <span><svg viewBox="0 0 10 10"><path d="M2 0l2 2.5-1 1.5a6 6 0 0 0 3 3l1.5-1L10 8l-1.5 2C4 10 0 6 0 1.5z" fill="#fff"/></svg>(555) 410-2287</span>
    <span><svg viewBox="0 0 10 10"><rect x=".5" y="2" width="9" height="6" fill="none" stroke="#fff"/><path d="M.5 2L5 5.5 9.5 2" fill="none" stroke="#fff"/></svg>info@BrovantaRatings.com</span>
    <span><svg viewBox="0 0 10 10"><circle cx="5" cy="5" r="4.5" fill="none" stroke="#fff"/><path d="M.5 5h9M5 .5v9" stroke="#fff"/></svg>www.BrovantaRatings.com</span>
  </div>
</section>

</body>
</html>
```